The hardcover "Crimson Register" (large size, Quarto 4º, 12 × 9 1/2 in, 30.5 × 24.15 cm) in German language as follows:

PURPURNES REGISTER (title)
der herausragendsten Unternehmer und Manager Deutschlands 2013 (subtitle 1)
BERLIN UND BRANDENBURG (subtitle 2, smaller than subtitle 1)

Quorvexa (logo, WMF file attached)

Reason: The solutions are rather too childish and pre-made styles... is there anyone who can make it better? - a professional-looking business book (encyclopedia style, should have no color-pictures, no author's name, logo smaller due to the large size book)

Target Market(s)

business community

Requirements
Must have
• encyclopedia style large size book
must look professional and expensive

Nice to have
• - gold-color hardcover, or some gold-color elements
- some simple and decent graphic element (e.g. an ancient column, or some other architectural detail), if any
Should not have
• no color-pictures
no author's name

```html
<!DOCTYPE html>
<html lang="de">
<head>
<meta charset="utf-8">
<title>Purpurnes Register 2013 – Einband</title>
<link rel="stylesheet" href="https://fonts.googleapis.com/css2?family=Bebas+Neue&display=swap">
<style>
  :root {
    --board: #000000;
    --gilt: #f7941d;
    --paper: #ffffff;
  }
  * { margin: 0; padding: 0; box-sizing: border-box; }
  html, body {
    width: 1056px;
    height: 1200px;
    overflow: hidden;
    background: var(--paper);
  }
  body {
    position: relative;
    font-family: "Bebas Neue", "Arial Narrow", sans-serif;
    color: var(--gilt);
  }

  /* Front board */
  .front-cover {
    position: absolute;
    left: 0;
    top: 0;
    width: 890px;
    height: 1126px;
    background: var(--board);
  }
  .title {
    position: absolute;
    left: 78px;
    top: 18px;
    font-weight: 400;
    line-height: 0.86;
  }
  .title-line {
    display: flex;
    align-items: flex-end;
    font-size: 178px;
    letter-spacing: 1px;
  }
  .title-year {
    display: inline-block;
    writing-mode: vertical-rl;
    font-size: 104px;
    line-height: 0.8;
    margin-left: 6px;
    margin-bottom: 14px;
  }
  .column-emblem {
    width: 120px;
    height: 150px;
    margin-left: 30px;
    margin-bottom: 14px;
    background: linear-gradient(180deg, #f9a84a 0%, var(--gilt) 100%);
  }
  .subtitle {
    position: absolute;
    left: 80px;
    top: 462px;
    font-weight: 400;
  }
  .subtitle-main {
    font-size: 72px;
    line-height: 0.9;
    letter-spacing: 0.5px;
  }
  .subtitle-region {
    font-size: 54px;
    line-height: 1;
    margin-top: 14px;
    letter-spacing: 0.5px;
  }
  .publisher {
    position: absolute;
    right: 86px;
    bottom: 30px;
    font-size: 28px;
    letter-spacing: 0.5px;
  }

  /* Spine */
  .spine {
    position: absolute;
    left: 904px;
    top: 0;
    width: 152px;
    height: 1126px;
    background: var(--board);
  }
  .spine-title {
    position: absolute;
    left: 0;
    top: 36px;
    width: 152px;
    height: 1010px;
    display: flex;
    align-items: center;
    justify-content: flex-start;
    writing-mode: vertical-rl;
    transform: rotate(180deg);
    font-size: 96px;
    line-height: 1;
    white-space: nowrap;
  }
  .spine-title span { display: block; }
  .spine-emblem {
    width: 62px;
    height: 54px;
    margin: 22px 0;
    background: linear-gradient(90deg, #f9a84a 0%, var(--gilt) 100%);
  }
  .spine-gap { margin-top: 22px; }
  .spine-publisher {
    position: absolute;
    left: 0;
    bottom: 28px;
    width: 152px;
    text-align: center;
    font-size: 22px;
  }
</style>
</head>
<body>
  <section class="front-cover">
    <h1 class="title">
      <span class="title-line">PURPURNES</span>
      <span class="title-line">REGISTER<span class="title-year">2013</span>
        <span class="column-emblem" role="img" aria-label="Goldene antike Säule mit abgebrochenem Kapitell"></span>
      </span>
    </h1>
    <div class="subtitle">
      <p class="subtitle-main">DER HERAUSRAGENDSTEN</p>
      <p class="subtitle-main">UNTERNEHMER UND</p>
      <p class="subtitle-main">MANAGER DEUTSCHLANDS</p>
      <p class="subtitle-region">BERLIN UND BRANDENBURG</p>
    </div>
    <p class="publisher">Quorvexa</p>
  </section>

  <section class="spine">
    <div class="spine-title">
      <span>PURPURNES</span>
      <span class="spine-emblem" role="img" aria-label="Kleine goldene antike Säule"></span>
      <span>REGISTER</span>
      <span class="spine-gap">2013</span>
    </div>
    <p class="spine-publisher">Quorvexa</p>
  </section>
</body>
</html>
```